Brightwater Dental
Stationary for Pediatric Dental & Orthodontics - Health
Stationary for Pediatric Dental & Orthodontics
Bright & Fun-filled
Pediatrics & Orthodontics
Larkspur Hollow Prof. Center 48517 Larkspur Hollow Ave. Suite B-07 Gaithersburg, MD 20886
info@brightwaterdental.org
www.brightwaterdental.org
I have uploaded the co logo to use for the card. I am looking for biz card (2 sided), appointment card, rewards biz card (can explain later, but basically the biz card with an offer on the back), referral pad, envelope (1 sided-no flap work), letterhead, & folder. I would also like to have a QR code linked to the company website on all materials, if it can be color and still work that would be great. I uploaded the static code that I have currently.
This only needs to be on the back of the biz card not the other materials........... Helping Children Who Need: Fillings, Braces, Crowns, Laughing Gas, Whitening, Mouthguards, Hospital Care, Special Needs Care, Clearvane, Nightguards, Cosmetics, Extractions, Walk-in Emergencies, Dental Home.................... Carewell and Most Insurances Accepted

```html
<!DOCTYPE html>
<html lang="en">
<head>
<meta charset="utf-8">
<title>Brightwater Dental – Business Card</title>
<link href="https://fonts.googleapis.com/css2?family=Nunito:wght@400;600;800&display=swap" rel="stylesheet">
<style>
  :root {
    --backdrop: #e4e5e7;
    --card: #ffffff;
    --brand-blue: #2a5dab;
    --brand-green: #8cc63f;
    --ink-light: #ffffff;
    --shadow: rgba(0,0,0,0.18);
  }
  html, body {
    margin: 0;
    padding: 0;
    width: 1200px;
    height: 951px;
    overflow: hidden;
    background: var(--backdrop);
    font-family: "Nunito", Arial, sans-serif;
  }
  .stage {
    position: relative;
    width: 1200px;
    height: 951px;
  }
  .card {
    position: absolute;
    width: 560px;
    height: 320px;
    background: var(--card);
    border-radius: 22px;
    overflow: hidden;
    box-shadow: 0 14px 30px var(--shadow);
  }
  .card--front { left: 500px; top: 100px; }
  .card--back  { left: 140px; top: 520px; }

  .wordmark {
    position: absolute;
    display: flex;
    flex-direction: column;
    align-items: flex-start;
  }
  .wordmark__row {
    display: flex;
    align-items: center;
    gap: 10px;
  }
  .wordmark__dot {
    width: 22px;
    height: 22px;
    border-radius: 50%;
    background: var(--brand-green);
  }
  .wordmark__name {
    font-weight: 800;
    color: var(--brand-blue);
    font-size: 38px;
    line-height: 1;
    letter-spacing: 0.5px;
  }
  .wordmark__tagline {
    margin-top: 6px;
    margin-left: 32px;
    font-weight: 600;
    font-size: 13px;
    color: var(--brand-blue);
    letter-spacing: 1px;
  }
  .card--front .wordmark { left: 70px; top: 128px; }
  .card--back .wordmark { left: 250px; top: 62px; }
  .card--back .wordmark__name { font-size: 28px; }
  .card--back .wordmark__dot { width: 16px; height: 16px; }
  .card--back .wordmark__tagline { font-size: 10px; margin-left: 26px; }

  .card__wave {
    position: absolute;
    inset: 0;
  }
  .contact {
    position: absolute;
    left: 26px;
    top: 128px;
    margin: 0;
    padding: 0;
    list-style: none;
    color: var(--ink-light);
    font-size: 11px;
    line-height: 21px;
  }
  .contact li {
    display: flex;
    align-items: center;
    gap: 9px;
  }
  .contact__icon {
    width: 9px;
    height: 9px;
    border-radius: 50%;
    background: var(--ink-light);
    flex: none;
  }
  .person {
    position: absolute;
    left: 352px;
    top: 205px;
    color: var(--brand-blue);
  }
  .person__name {
    font-size: 17px;
    font-weight: 600;
    margin: 0;
  }
  .person__role {
    font-size: 13px;
    margin: 2px 0 0;
  }
</style>
</head>
<body>
<main class="stage">
  <section class="card card--front" aria-label="Business card front">
    <div class="wordmark">
      <div class="wordmark__row">
        <span class="wordmark__dot"></span>
        <span class="wordmark__name">Brightwater Dental</span>
      </div>
      <span class="wordmark__tagline">Pediatrics &amp; Orthodontics</span>
    </div>
  </section>

  <section class="card card--back" aria-label="Business card back">
    <svg class="card__wave" viewBox="0 0 560 320" width="560" height="320" aria-hidden="true">
      <path d="M0,44 C110,8 215,40 245,130 C275,230 370,285 560,282"
            fill="none" stroke="var(--brand-green)" stroke-width="7"/>
      <path d="M0,56 C115,22 225,55 252,145 C282,240 380,292 560,292"
            fill="none" stroke="var(--brand-blue)" stroke-width="3"/>
      <path d="M0,70 C115,38 230,70 258,160 C288,255 385,302 560,302 L560,320 L0,320 Z"
            fill="var(--brand-blue)"/>
    </svg>

    <div class="wordmark">
      <div class="wordmark__row">
        <span class="wordmark__dot"></span>
        <span class="wordmark__name">Brightwater Dental</span>
      </div>
      <span class="wordmark__tagline">Pediatrics &amp; Orthodontics</span>
    </div>

    <ul class="contact">
      <li><span class="contact__icon"></span>Suite B-07, Larkspur Ave.</li>
      <li><span class="contact__icon"></span>Gaithersburg, MD</li>
      <li><span class="contact__icon"></span>301 555 0142</li>
      <li><span class="contact__icon"></span>301 555 0187</li>
      <li><span class="contact__icon"></span>info@brightwaterdental.org</li>
      <li><span class="contact__icon"></span>www.brightwaterdental.org</li>
    </ul>

    <div class="person">
      <p class="person__name">Evan Marsh</p>
      <p class="person__role">Owner / C.E.O</p>
    </div>
  </section>
</main>
</body>
</html>
```